medical equipment home page redesign

We need a new home page for an existing store. We'll be redoing the entire site to make it more user friendly and follow talequill guidelines. We have a loose wireframe for the sections, but need help making it look great. The look should be clean, modern, professional, etc. We have a background image we would like to incorporate somewhere because we've just printed business cards and brochures that use this background image. We love parallax effects on backgrounds, so please allow extra big background images so we can utilize that effect. You can find images, etc from our site at brivolune.com. We like the way this site feels: http://tkro.palvenix.com/home/page/venue with the parallax background. And this one, too: https://www.muddersheriot.org/

Target Market(s)

people with chronic pain

Industry/Entity Type

Medical Equipment

Number of Pages Required

1 page

Font styles to use
Sans Serif

Colors
b8a6cd
6b449b
e4daeb

Requirements
Must have
• Please include sections from our wireframe. They don't have to look like the wireframe, but they do need to portray that information in each section.
Nice to have
• It would be great if you could include the background image we have attached
Should not have
• Should not look like the old site.

```html
<!DOCTYPE html>
<html lang="en">
<head>
<meta charset="utf-8">
<title>Brivolune — Light Your Way Out of Pain</title>
<link rel="stylesheet" href="https://fonts.googleapis.com/css2?family=Raleway:wght@300;400;500&family=Lato:wght@400&display=swap">
<style>
  :root {
    --lavender: #b8a6cd;
    --purple: #6b449b;
    --mist: #e4daeb;
    --paper: #f4eff7;
    --white: #ffffff;
    --ink: #2f2a33;
    --soft-ink: #55505a;
    --band: rgba(107, 68, 155, 0.72);
  }
  * { box-sizing: border-box; margin: 0; padding: 0; }
  html, body { width: 1200px; height: 3000px; overflow: hidden; }
  body { font-family: "Raleway", Arial, sans-serif; color: var(--ink); background: var(--paper); position: relative; }
  section, header, footer { position: absolute; left: 0; width: 1200px; }

  /* Header */
  .site-header { top: 0; height: 75px; background: var(--mist); border-bottom: 1px solid #cfc2da; }
  .brand { position: absolute; left: 151px; top: 8px; height: 60px; display: flex; align-items: center; gap: 8px; }
  .brand-dot { width: 16px; height: 16px; border-radius: 50%; background: var(--purple); }
  .brand-name { font-size: 24px; font-weight: 500; color: var(--purple); }
  .main-nav { position: absolute; right: 150px; top: 26px; display: flex; align-items: center; gap: 14px; font-size: 11px; color: var(--soft-ink); text-transform: uppercase; }
  .main-nav .nav-shop { margin-left: 32px; background: var(--purple); color: var(--white); padding: 4px 6px; border-radius: 12px; }

  /* Hero */
  .hero { top: 75px; height: 263px; text-align: center; color: var(--white);
    background: radial-gradient(circle at 2% 75%, #fff6d8 0, #f9c67a 12%, transparent 40%),
                linear-gradient(100deg, #f3b25e 0%, #e9844a 35%, #d96a4f 60%, #b77f8a 85%, #9e8fb2 100%); }
  .hero-title { position: absolute; top: 30px; width: 100%; font-size: 33px; font-weight: 400; letter-spacing: 0.5px; }
  .hero-sub { position: absolute; top: 86px; width: 100%; font-size: 17px; font-weight: 300; }
  .hero-btn { position: absolute; left: 544px; top: 130px; width: 112px; height: 43px; border: 1.5px solid var(--white); border-radius: 22px; line-height: 40px; font-size: 14px; }
  .hero-tagline { position: absolute; top: 200px; width: 100%; font-size: 32px; font-weight: 300; letter-spacing: 1px; opacity: 0.85; }
  .hero-tagline span { margin: 0 14px; }

  /* Section headings */
  .section-title { position: absolute; width: 100%; text-align: center; font-size: 23px; font-weight: 400; }
  .section-title span { color: var(--lavender); }

  /* Image cards */
  .card { position: absolute; border-radius: 4px; overflow: hidden; }
  .card-label { position: absolute; left: 0; right: 0; bottom: 0; background: var(--band); color: var(--white); text-align: center; font-size: 19px; }

  .therapies { top: 338px; height: 295px; background: var(--paper); }
  .therapies .card { top: 78px; height: 187px; }
  .therapies .card-label { height: 37px; line-height: 37px; }
  .fill-pbm { background: linear-gradient(#5c5a5a, #c81b34 70%, #e82945); }
  .fill-green { background: linear-gradient(135deg, #2b3a2c, #1ea85a 55%, #6fe08f); }
  .fill-blue { background: linear-gradient(135deg, #4a4a55, #9a8c88 50%, #3b3f6a); }
  .fill-red { background: radial-gradient(circle at 60% 55%, #fde5f2 0, #f02a7d 35%, #6a0b2a 100%); }

  /* Testimonials */
  .testimonials { top: 633px; height: 374px; background: var(--white); }
  .quote-mark { position: absolute; font-family: Georgia, serif; font-size: 130px; line-height: 1; color: var(--lavender); }
  .quote-open { left: 150px; top: 66px; }
  .quote-close { left: 966px; top: 124px; }
  .quote-text { position: absolute; left: 225px; width: 750px; top: 80px; text-align: center; font-family: "Lato", Arial, sans-serif; font-size: 14.5px; line-height: 30px; color: var(--ink); }
  .reviewer { position: absolute; top: 270px; display: flex; align-items: center; gap: 14px; }
  .avatar { width: 75px; height: 75px; border-radius: 50%; }
  .reviewer-name { font-size: 17px; color: var(--soft-ink); }
  .reviewer-role { font-size: 12px; color: var(--lavender); }

  /* Pets */
  .audiences { top: 1007px; height: 397px; background: var(--paper); }
  .audiences .card { top: 76px; height: 292px; }
  .audiences .card-label { height: 56px; line-height: 56px; }
  .fill-people { background: linear-gradient(135deg, #6b5a52, #d8a890 45%, #3a3040); }
  .fill-horses { background: linear-gradient(135deg, #7b8a5c, #9a6a44 45%, #c9453c); }
  .fill-dogs { background: linear-gradient(135deg, #5b6a58, #e8e2dc 45%, #2a2426); }

  /* Featured products */
  .featured { top: 1404px; height: 320px; background: var(--white); }
  .featured .card { top: 87px; height: 187px; }
  .slider-arrow { position: absolute; top: 160px; }
  .slider-dots { position: absolute; top: 280px; left: 567px; display: flex; gap: 5px; }
  .slider-dots i { width: 9px; height: 9px; border-radius: 50%; border: 1px solid var(--purple); }
  .slider-dots i.active { background: var(--purple); }

  /* Video */
  .video { top: 1724px; height: 613px; background: var(--paper); }
  .video-frame { position: absolute; left: 150px; top: 77px; width: 900px; height: 506px; background: var(--lavender); border-radius: 4px; }
  .video-frame svg { position: absolute; left: 390px; top: 193px; }

  /* Blog */
  .blog { top: 2337px; height: 331px; background: var(--white); }
  .blog-card { position: absolute; top: 77px; height: 225px; background: var(--purple); border-radius: 4px; }

  /* Footer */
  .site-footer { top: 2668px; height: 332px; background: var(--lavender); font-size: 10.5px; }
  .footer-col { position: absolute; top: 89px; list-style: none; line-height: 18px; }
  .footer-col.company { left: 151px; color: var(--white); }
  .footer-col.company li:first-child { margin-bottom: 14px; }
  .footer-col.company li + li { color: var(--purple); }
  .footer-col.policies { left: 243px; color: var(--purple); }
  .social { position: absolute; left: 510px; top: 142px; display: flex; gap: 15px; }
  .social a { width: 34px; height: 34px; border-radius: 50%; background: #8d70b8; display: block; }
  .newsletter-label { position: absolute; left: 693px; top: 98px; font-size: 13px; color: var(--purple); }
  .newsletter { position: absolute; left: 693px; top: 127px; width: 357px; height: 55px; display: flex; border-radius: 4px; overflow: hidden; }
  .newsletter-input { flex: 1; background: #f6f2f9; color: var(--soft-ink); font-size: 13px; padding-left: 16px; line-height: 55px; }
  .newsletter-btn { width: 94px; background: var(--purple); color: var(--white); font-size: 14px; text-align: center; line-height: 55px; }
  .copyright { position: absolute; bottom: 12px; width: 100%; text-align: center; font-size: 9px; color: var(--purple); }
</style>
</head>
<body>

<header class="site-header">
  <div class="brand"><span class="brand-dot"></span><span class="brand-name">Brivolune</span></div>
  <nav class="main-nav">
    <span>Home</span><span>What's New</span><span>About Us</span><span class="nav-shop">Shop Now</span>
  </nav>
</header>

<section class="hero" role="img" aria-label="Warm sunset sky background">
  <h1 class="hero-title">Light Your Way Out of Pain</h1>
  <p class="hero-sub">Because everyone deserves access to a pain free life</p>
  <div class="hero-btn">SHOP NOW</div>
  <p class="hero-tagline"><span>Drug Free.</span><span>Safe.</span><span>Pain Relief.</span></p>
</section>

<section class="therapies">
  <h2 class="section-title" style="top:27px">HOW LIGHT THERAPY CAN <span>STOP YOUR PAIN</span></h2>
  <div class="card fill-pbm" style="left:150px;width:219px" role="img" aria-label="Red PBM light device"><div class="card-label">PBM</div></div>
  <div class="card fill-green" style="left:377px;width:219px" role="img" aria-label="Green light shining through water"><div class="card-label">Green</div></div>
  <div class="card fill-blue" style="left:603px;width:219px" role="img" aria-label="Blue light applied to a jaw"><div class="card-label">Blue</div></div>
  <div class="card fill-red" style="left:830px;width:220px" role="img" aria-label="Red light glowing through hair"><div class="card-label">Red</div></div>
</section>

<section class="testimonials">
  <h2 class="section-title" style="top:26px">CUSTOMER <span>TESTIMONIALS</span></h2>
  <div class="quote-mark quote-open">&ldquo;</div>
  <p class="quote-text">“Fantastic treatment systems. Every family practitioner should have one.&nbsp; Cost effective for patients and doctor. Every patient wants a speedy recovery, to get better fast. The improvement in patients pain and healing is substantial. Fabulous engineering.&nbsp; Super simple to use. Highly recommend this treatment system to any family practice physician or specialist looking to add cost effective photobiomodulation therapy to their practice routines.”</p>
  <div class="quote-mark quote-close">&rdquo;</div>
  <div class="reviewer" style="left:150px">
    <div class="avatar" style="background:#d9cfdf" role="img" aria-label="Portrait of Lena"></div>
    <div><div class="reviewer-name">Lena</div><div class="reviewer-role">Brackwell, Ohio</div></div>
  </div>
  <div class="reviewer" style="left:450px">
    <div class="avatar" style="background:#a89a90" role="img" aria-label="Portrait of Warren D. Holcomb"></div>
    <div><div class="reviewer-name">Warren D. Holcomb</div><div class="reviewer-role">MD,MS,FAAEP</div></div>
  </div>
  <div class="reviewer" style="left:796px">
    <div class="avatar" style="background:#c7c3c9" role="img" aria-label="Portrait of Maren K. Ostby"></div>
    <div><div class="reviewer-name">Maren K. Ostby</div><div class="reviewer-role">Professor Biomedical Sciences</div></div>
  </div>
</section>

<section class="audiences">
  <h2 class="section-title" style="top:26px">LIGHT THERAPY FOR <span>YOU &amp; YOUR PETS</span></h2>
  <div class="card fill-people" style="left:150px;width:292px" role="img" aria-label="Two women smiling together"><div class="card-label">People</div></div>
  <div class="card fill-horses" style="left:453px;width:293px" role="img" aria-label="Horse receiving light therapy"><div class="card-label">Horses</div></div>
  <div class="card fill-dogs" style="left:757px;width:293px" role="img" aria-label="Small dog receiving light therapy"><div class="card-label">Dogs</div></div>
</section>

<section class="featured">
  <h2 class="section-title" style="top:34px">FEATURED <span>PRODUCTS</span></h2>
  <svg class="slider-arrow" style="left:119px" width="26" height="50" viewBox="0 0 26 50"><path d="M24 2 L3 25 L24 48" fill="none" stroke="#6b449b" stroke-width="2"/></svg>
  <div class="card fill-pbm" style="left:150px;width:219px" role="img" aria-label="PBM light device product"></div>
  <div class="card fill-green" style="left:377px;width:219px" role="img" aria-label="Green light device product"></div>
  <div class="card fill-blue" style="left:603px;width:219px" role="img" aria-label="Blue light device product"></div>
  <div class="card fill-red" style="left:830px;width:220px" role="img" aria-label="Red light device product"></div>
  <svg class="slider-arrow" style="left:1056px" width="26" height="50" viewBox="0 0 26 50"><path d="M2 2 L23 25 L2 48" fill="none" stroke="#6b449b" stroke-width="2"/></svg>
  <div class="slider-dots"><i class="active"></i><i></i><i></i><i></i><i></i></div>
</section>

<section class="video">
  <h2 class="section-title" style="top:28px">INFORMATIVE <span>VIDEO</span></h2>
  <div class="video-frame" role="img" aria-label="Informative video player">
    <svg width="120" height="120" viewBox="0 0 120 120"><circle cx="60" cy="60" r="55" fill="none" stroke="#2f2a33" stroke-width="4"/><path d="M47 38 L85 60 L47 82 Z" fill="none" stroke="#2f2a33" stroke-width="4" stroke-linejoin="round"/></svg>
  </div>
</section>

<section class="blog">
  <h2 class="section-title" style="top:25px">OUR <span>BLOG</span></h2>
  <div class="blog-card" style="left:150px;width:292px"></div>
  <div class="blog-card" style="left:453px;width:293px"></div>
  <div class="blog-card" style="left:757px;width:293px"></div>
</section>

<footer class="site-footer">
  <ul class="footer-col company">
    <li>Brivolune</li><li>FAQ's</li><li>About Us</li><li>Contact Us</li>
  </ul>
  <ul class="footer-col policies">
    <li>Lifetime Product Warranty</li><li>No-Worries Guarantee</li><li>Disclaimer</li><li>Terms of Use</li><li>GDPR Privacy Policy</li>
  </ul>
  <div class="social"><a aria-label="Social link one"></a><a aria-label="Social link two"></a><a aria-label="Social link three"></a></div>
  <p class="newsletter-label">Join Our Newsletter</p>
  <div class="newsletter"><div class="newsletter-input">Email...</div><div class="newsletter-btn">Sign Up</div></div>
  <p class="copyright">©2019 Brivolune</p>
</footer>

</body>
</html>
```